doctor needs a professional business card

please use the attached logo for the design.
Information for the card:
Loretta V Brandwick, MD
4381 Fallow Crest Clinical Way Drive
Wilmington NC 28517
phone 910.586.2741
fax 910.586.2799
practice web site address- brandwickvue.net
Target Market(s)
55 to 80 years old
Industry/Entity Type
Business

```html
<!DOCTYPE html>
<html lang="en">
<head>
<meta charset="utf-8">
<title>Brandwick Vue – Business Card</title>
<link href="https://fonts.googleapis.com/css2?family=Exo+2:wght@500;600&family=Open+Sans:wght@400;600&display=swap" rel="stylesheet">
<style>
  :root {
    --navy: #3f5b8a;
    --frame: #a3a3a3;
    --charcoal: #4a4a4a;
    --ink: #3d3d3d;
    --paper: #ffffff;
    --backdrop: #d6d6d6;
  }
  * { box-sizing: border-box; margin: 0; padding: 0; }
  html, body {
    width: 1200px; height: 894px; overflow: hidden;
    background: var(--backdrop);
    font-family: "Open Sans", Arial, sans-serif;
  }
  .canvas { position: relative; width: 1200px; height: 894px; }

  .card {
    position: absolute; left: 240px;
    width: 720px; height: 412px;
    background: var(--paper);
    overflow: hidden;
    box-shadow: 0 6px 18px rgba(0,0,0,.18);
  }
  .card--back { top: 24px; }
  .card--front { top: 458px; }

  .card__frame {
    position: absolute; inset: 16px;
    border: 3px solid var(--frame);
    z-index: 1;
  }

  .brand {
    position: absolute; display: flex; align-items: center; gap: 14px;
    color: var(--navy); font-weight: 600; z-index: 2;
  }
  .brand__dot { width: 30px; height: 30px; border-radius: 50%; background: var(--navy); }

  /* back */
  .card--back .brand { left: 0; right: 0; top: 118px; justify-content: center; font-size: 46px; }
  .card--back .band {
    position: absolute; left: 0; right: 0; top: 250px; height: 86px;
    background: var(--navy); z-index: 2;
    display: flex; align-items: center; justify-content: center;
  }
  .band__web { color: #fff; font-size: 26px; letter-spacing: 1.5px; }

  /* front */
  .card--front .brand { left: 64px; top: 44px; font-size: 36px; }
  .card--front .band {
    position: absolute; left: 0; right: 0; bottom: 0; height: 64px;
    background: var(--navy); z-index: 0;
  }
  .card--front .tab {
    position: absolute; left: 0; bottom: 64px; width: 120px; height: 36px;
    background: var(--charcoal); z-index: 0;
  }
  .contact {
    position: absolute; display: flex; align-items: flex-start; gap: 12px;
    color: var(--ink); font-size: 16px; line-height: 1.4; z-index: 2;
  }
  .contact__icon {
    flex: none; width: 26px; height: 26px; border-radius: 5px;
    background: var(--navy); display: flex; align-items: center; justify-content: center;
  }
  .contact__icon svg { width: 16px; height: 16px; }
  .contact__label { color: var(--navy); font-weight: 600; margin-right: 4px; }
  .contact--phone { left: 64px; top: 140px; }
  .contact--fax { left: 64px; top: 180px; }
  .contact--email { left: 64px; top: 220px; }
  .contact--address { left: 392px; top: 218px; }
  .contact--address span:last-child { max-width: 250px; }
  .contact--web { left: 392px; top: 300px; }

  .person { position: absolute; left: 392px; top: 136px; z-index: 2; font-family: "Exo 2", Arial, sans-serif; }
  .person__name { color: var(--navy); font-size: 25px; font-weight: 600; }
  .person__title { color: var(--navy); font-size: 17px; font-weight: 500; margin-top: 2px; }
</style>
</head>
<body>
<main class="canvas">

  <section class="card card--back" aria-label="Business card, back">
    <div class="card__frame"></div>
    <div class="brand"><span class="brand__dot"></span><span class="brand__name">Brandwick Vue</span></div>
    <div class="band"><span class="band__web">www.brandwickvue.net</span></div>
  </section>

  <section class="card card--front" aria-label="Business card, front">
    <div class="band"></div>
    <div class="tab"></div>
    <div class="card__frame"></div>

    <div class="brand"><span class="brand__dot"></span><span class="brand__name">Brandwick Vue</span></div>

    <div class="contact contact--phone">
      <span class="contact__icon">
        <svg viewBox="0 0 16 16"><path fill="#fff" d="M4 1.5l2 3-1.3 1.5c.8 1.8 2.3 3.3 4.3 4.3L10.5 9l3 2-1 2.6C7 13.5 2.5 9 2.4 3.5z"/></svg>
      </span>
      <span><span class="contact__label">P</span>910.586.2741</span>
    </div>
    <div class="contact contact--fax">
      <span class="contact__icon">
        <svg viewBox="0 0 16 16"><rect x="4" y="2" width="8" height="4" fill="none" stroke="#fff" stroke-width="1.3"/><rect x="2" y="6" width="12" height="6" fill="#fff"/><rect x="4.5" y="10" width="7" height="4" fill="#fff" stroke="#3f5b8a" stroke-width="1"/></svg>
      </span>
      <span><span class="contact__label">F</span>910.586.2799</span>
    </div>
    <div class="contact contact--email">
      <span class="contact__icon">
        <svg viewBox="0 0 16 16"><rect x="2" y="4" width="12" height="8" fill="none" stroke="#fff" stroke-width="1.4"/><path d="M2 4l6 5 6-5" fill="none" stroke="#fff" stroke-width="1.4"/></svg>
      </span>
      <span>office@brandwickvue.net</span>
    </div>

    <div class="person">
      <div class="person__name">Loretta V Brandwick, MD</div>
      <div class="person__title">Ophthalmologist</div>
    </div>

    <div class="contact contact--address">
      <span class="contact__icon">
        <svg viewBox="0 0 16 16"><path fill="#fff" d="M8 1a4.5 4.5 0 0 0-4.5 4.5C3.5 9 8 15 8 15s4.5-6 4.5-9.5A4.5 4.5 0 0 0 8 1zm0 6.2a1.8 1.8 0 1 1 0-3.6 1.8 1.8 0 0 1 0 3.6z"/></svg>
      </span>
      <span>4381 Fallow Crest<br>Clinical Way Drive<br>Wilmington NC 28517</span>
    </div>
    <div class="contact contact--web">
      <span class="contact__icon">
        <svg viewBox="0 0 16 16"><circle cx="8" cy="8" r="6" fill="none" stroke="#fff" stroke-width="1.3"/><ellipse cx="8" cy="8" rx="2.6" ry="6" fill="none" stroke="#fff" stroke-width="1.1"/><path d="M2 8h12" stroke="#fff" stroke-width="1.1"/></svg>
      </span>
      <span>www.brandwickvue.net</span>
    </div>
  </section>

</main>
</body>
</html>
```